The Bright Meadow Foundation

This is a non profit . We are a 501(c)(3) charitable organization in the United States. The organization is a volunteer based group providing basic healthcare to those living in underserved rural areas around the world. I have attached a brochure that provides some information about the organization. We are looking for a basic 5 page web page Page 1 Photos that fade into the next x 3 with mission statementPage 2 About us - details about bright meadow foundation. also introducing our Founders of the organization. Marina Kellet, M.D. Dorla Penn , FNP, Rosa Tembley, FNP, Wade Marlow. ( will provide you info on each.Page 3 Projects coming up and futurePage 4 Get involved - Give a donation, Volunteer, Corporate supportPage 5 Support us and contact us with a message box.We mainly work in South America but anticipate trave to South Africa in the near future. Colors bright with emphasis on Reds and Purples. I have attached some photos and ideas. You can use or not use ok to use something similar if you so like

Target Market(s)

People interested in volunteering time or money to overseas medical work. NOT a religious base

Coding

Coded - Design and coding required

Number of Pages Required

1 page

Colors
876aae
ec1f27
f37022
9bcb3c

Requirements
Must have
• Colorful pictures nature, brings out emotion, colorful, children from various parts of the world, animals.
• Tried to down load some pictures but would not go thru.

```html
<!DOCTYPE html>
<html lang="en">
<head>
<meta charset="utf-8">
<title>Bright Meadow Foundation</title>
<link rel="stylesheet" href="https://fonts.googleapis.com/css2?family=Raleway:wght@400;500;600;700;800&family=Open+Sans:wght@400;600;700&display=swap">
<style>
:root{
  --purple:#876aae;
  --purple-deep:#7a4fa6;
  --purple-night:#4a1e6a;
  --red:#ec1f27;
  --orange:#f37022;
  --green:#9bcb3c;
  --ink:#222222;
  --text:#555555;
  --white:#ffffff;
}
*{box-sizing:border-box;margin:0;padding:0}
html,body{width:1200px;height:5099px;overflow:hidden;background:var(--white)}
body{position:relative;font-family:"Open Sans",Arial,sans-serif;color:var(--text)}
.abs{position:absolute}
h1,h2,h3,.nav,.brand{font-family:"Raleway",Arial,sans-serif}
.photo{position:absolute}

/* header */
.site-header{position:absolute;left:0;top:0;width:1200px;height:72px}
.brand{position:absolute;left:153px;top:14px;display:flex;align-items:center;gap:8px;font-weight:700;font-size:15px;color:var(--purple-deep)}
.brand-dot{width:22px;height:22px;border-radius:50%;background:var(--red)}
.top-call{position:absolute;left:890px;top:10px;font-size:10px;color:var(--red);font-weight:600}
.social-dot{position:absolute;top:8px;width:14px;height:14px;border-radius:50%}
.nav{position:absolute;left:476px;top:44px;display:flex;gap:34px;font-size:12px;font-weight:700;color:var(--ink);letter-spacing:.3px}
.nav span.active{border-bottom:2px solid var(--red);padding-bottom:3px}

/* hero */
.hero-photo{left:153px;top:75px;width:952px;height:367px;background:linear-gradient(180deg,#9fc0e0 0%,#c9d8e6 30%,#6a5fa0 55%,#5d4a8f 75%,#3f6b2c 100%)}
.hero-title{position:absolute;left:212px;top:150px;color:var(--white);font-weight:800;font-size:46px;line-height:44px;letter-spacing:1px}
.hero-title small{display:block;font-size:16px;line-height:20px;font-weight:700;letter-spacing:1px;padding-left:130px}
.donate-box{position:absolute;left:210px;top:289px;width:300px;height:153px;background:var(--red);padding:14px 20px;color:var(--white)}
.donate-box h3{font-size:16px;font-weight:800;letter-spacing:.5px}
.donate-box p{font-size:10px;line-height:14px;margin-top:8px}
.donate-box .btns{display:flex;gap:14px;margin-top:16px}
.donate-box .btn-mini{font-size:9px;font-weight:700;padding:7px 12px;background:var(--orange)}

/* headings & buttons */
.mission-heading{position:absolute;left:102px;top:585px;font-size:50px;font-weight:700;color:var(--purple-deep);letter-spacing:1px}
.section-title{font-family:"Raleway",Arial,sans-serif;font-size:38px;font-weight:600;color:var(--ink);line-height:46px}
.body-text{font-size:13px;line-height:21px;color:var(--text);margin-top:20px}
.cta{display:flex;margin-top:28px;height:30px}
.cta .label{background:var(--orange);color:var(--white);font-size:10px;font-weight:700;padding:0 18px;display:flex;align-items:center;letter-spacing:.5px}
.cta .arrow{width:40px;background:#111;display:flex;align-items:center;justify-content:center}
.cta-row{display:flex;gap:24px}

/* about cards */
.card{position:absolute;top:4165px;width:204px;height:408px;background:var(--purple);color:var(--white);text-align:center;padding-top:12px}
.card .avatar{width:120px;height:120px;border-radius:50%;margin:0 auto;border:6px solid var(--white);background:linear-gradient(160deg,#d8b49a,#8c5a48)}
.card h3{font-size:13px;font-weight:700;margin-top:16px}
.card .role{font-size:11px;margin-top:3px}
.card p{font-size:10.5px;line-height:16px;padding:0 18px;margin-top:10px}
.card .bio-btn{display:inline-block;margin-top:14px;border:1px solid var(--white);font-size:10px;padding:6px 18px}

/* footer */
.contact-area{position:absolute;left:0;top:4641px;width:1200px;height:458px;background:var(--purple-night);color:var(--white)}
.contact-area h2{position:absolute;width:1200px;top:50px;text-align:center;font-size:40px;font-weight:700}
.col-title{position:absolute;font-size:13px;font-weight:700}
.col-list{position:absolute;font-size:11px;line-height:22px}
.field{position:absolute;left:809px;width:238px;border-bottom:1px solid rgba(255,255,255,.7);font-size:11px;padding-bottom:4px}
</style>
</head>
<body>

<header class="site-header">
  <div class="brand"><span class="brand-dot"></span>Bright Meadow Foundation</div>
  <div class="top-call">Call: 1-555-014-2290</div>
  <span class="social-dot" style="left:1012px;background:var(--green)" aria-label="Circle Social"></span>
  <span class="social-dot" style="left:1034px;background:var(--red)" aria-label="Snapframe"></span>
  <nav class="nav"><span class="active">HOME</span><span>MISSION</span><span>FUTURE</span><span>GET INVOLVED</span><span>ABOUT</span><span>CONTACT US</span></nav>
</header>

<!-- hero -->
<div class="abs" style="left:102px;top:153px;width:51px;height:340px;background:var(--green)"></div>
<div class="photo hero-photo" role="img" aria-label="Field of purple lupine flowers below snowy mountains"></div>
<div class="abs" style="left:1020px;top:68px;width:85px;height:136px;background:var(--red)"></div>
<div class="abs" style="left:990px;top:108px;width:130px;height:40px;background:var(--red)"></div>
<div class="abs" style="left:867px;top:384px;width:290px;height:58px;background:var(--orange)"></div>
<h1 class="hero-title">BRIGHT<br>MEADOW<small>FOUNDATION</small></h1>
<div class="donate-box">
  <h3>DONATE FOR A GOOD CAUSE</h3>
  <p>Your donations allow us to provide medical care, health resources and supplies, and wellness education to communities we serve.</p>
  <div class="btns"><span class="btn-mini">DONATE NOW</span><span class="btn-mini">LEARN MORE</span></div>
</div>

<!-- mission statement -->
<h2 class="mission-heading">MISSION STATEMENT</h2>
<svg class="abs" style="left:695px;top:578px" width="100" height="80" viewBox="0 0 100 80" aria-hidden="true">
  <path d="M50 76 C20 55 4 40 4 22 C4 10 14 2 26 2 C37 2 45 9 50 17 C55 9 63 2 74 2 C86 2 96 10 96 22 C96 40 80 55 50 76Z" fill="var(--red)"/>
  <polyline points="10,40 34,40 42,26 50,56 58,34 64,40 90,40" fill="none" stroke="#fff" stroke-width="4" stroke-linejoin="round"/>
</svg>

<section class="abs" style="left:153px;top:731px;width:290px">
  <h2 class="section-title">Our Mission</h2>
  <p class="body-text">The Bright Meadow Foundation was founded with the aim of helping rural and indigenous individuals in various parts of the world. The Foundation's vision is to see that every woman, man and child have access to basic medical care and treatment as well as fundamental knowledge in preventative care.</p>
  <div class="cta"><span class="label">KNOW MORE</span><span class="arrow"><svg width="16" height="10"><path d="M0 5h14M10 1l4 4-4 4" stroke="#fff" stroke-width="1.6" fill="none"/></svg></span></div>
</section>
<div class="photo" style="left:469px;top:697px;width:578px;height:384px;background:linear-gradient(135deg,#c23b6a,#e59a3a 50%,#6b3a2a)" role="img" aria-label="Woman in colourful traditional dress holding a small child"></div>

<!-- projects -->
<div class="photo" style="left:153px;top:1183px;width:571px;height:388px;background:radial-gradient(circle at 40% 45%,#d2392e 0%,#c33 20%,#4f8a2c 55%,#2e5f1f 100%)" role="img" aria-label="Red macaw perched on a branch among green leaves"></div>
<div class="abs" style="left:1156px;top:1224px;width:44px;height:204px;background:var(--green)"></div>
<div class="abs" style="left:724px;top:1537px;width:476px;height:68px;background:var(--purple)"></div>
<section class="abs" style="left:748px;top:1207px;width:300px">
  <h2 class="section-title">Projects coming up and future</h2>
  <p class="body-text">We are committed to increasing the health and welfare of our global community. The Foundation will continue to expand work into other rural areas of both Central and South America.</p>
  <div class="cta"><span class="label">KNOW MORE</span><span class="arrow"><svg width="16" height="10"><path d="M0 5h14M10 1l4 4-4 4" stroke="#fff" stroke-width="1.6" fill="none"/></svg></span></div>
</section>

<!-- get involved -->
<div class="abs" style="left:0;top:1836px;width:136px;height:272px;background:var(--red)"></div>
<div class="photo" style="left:153px;top:1734px;width:428px;height:220px;background:linear-gradient(135deg,#8a5a3c,#c99a70 55%,#6b4030)" role="img" aria-label="Two smiling young children"></div>
<div class="photo" style="left:355px;top:1890px;width:315px;height:190px;background:linear-gradient(135deg,#7a3b2e,#c25a3a 50%,#3b2a3e)" role="img" aria-label="Elder woman in traditional colourful clothing"></div>
<div class="abs" style="left:153px;top:2057px;width:204px;height:112px;background:var(--green)"></div>
<svg class="abs" style="left:217px;top:2079px" width="70" height="66" viewBox="0 0 70 66" aria-hidden="true">
  <circle cx="35" cy="33" r="30" fill="#fff"/>
  <path d="M35 52 C20 42 14 34 14 26 C14 19 19 15 25 15 C30 15 33 18 35 22 C37 18 40 15 45 15 C51 15 56 19 56 26 C56 34 50 42 35 52Z" fill="var(--purple)"/>
</svg>
<section class="abs" style="left:639px;top:1741px;width:408px;height:428px;border:2px solid var(--orange);padding:36px 56px 0 56px;background:var(--white)">
  <h2 class="section-title">Get involved -<br>Give a donation</h2>
  <p class="body-text">There are many people living in regions of the world today who have limited or no access to health centers. Often, these individuals travel hours and in many instances days for basic care that often times can be amended with preventative care measures.</p>
  <div class="cta-row">
    <div class="cta"><span class="label">KNOW MORE</span><span class="arrow"><svg width="16" height="10"><path d="M0 5h14M10 1l4 4-4 4" stroke="#fff" stroke-width="1.6" fill="none"/></svg></span></div>
    <div class="cta"><span class="label">DONATE</span><span class="arrow"><svg width="16" height="10"><path d="M0 5h14M10 1l4 4-4 4" stroke="#fff" stroke-width="1.6" fill="none"/></svg></span></div>
  </div>
</section>

<!-- volunteer -->
<div class="abs" style="left:92px;top:2312px;width:955px;height:398px;background:var(--purple)"></div>
<div class="photo" style="left:510px;top:2244px;width:540px;height:466px;background:linear-gradient(180deg,rgba(255,255,255,0) 0%,#3fb8d6 45%,#2a8fb0 100%)" role="img" aria-label="Four smiling volunteers in blue shirts holding a globe with a heart"></div>
<section class="abs" style="left:150px;top:2360px;width:300px;color:var(--white)">
  <h2 class="section-title" style="color:var(--white)">Volunteer</h2>
  <p class="body-text" style="color:var(--white)">Creating a more comprehensive medical team of volunteers and resources both from the United States as well as other countries and from local communities is a component of the organization's long term goals.</p>
  <div class="cta"><span class="label">JOIN US</span><span class="arrow"><svg width="16" height="10"><path d="M0 5h14M10 1l4 4-4 4" stroke="#fff" stroke-width="1.6" fill="none"/></svg></span></div>
</section>

<!-- partner -->
<div class="photo" style="left:0;top:2829px;width:1200px;height:520px;background:linear-gradient(180deg,#2c4f8c 0%,#5f86b8 35%,#3d6a3a 70%,#2a3f2a 100%)" role="img" aria-label="Mountain valley landscape with a red bromeliad flower in the foreground"></div>
<div class="abs" style="left:0;top:3349px;width:663px;height:41px;background:var(--orange)"></div>
<section class="abs" style="left:700px;top:2895px;width:350px;color:var(--white)">
  <h2 class="section-title" style="color:var(--white)">Partner with us</h2>
  <p class="body-text" style="color:var(--white)">The Foundation will continue to expand work into other rural areas of both Central and South America. In addition, We are currently working on a partnership with a nongovernmental organization in South Africa and hope to be expanding to this part of the globe in the near future.</p>
  <div class="cta"><span class="label">JOIN US</span><span class="arrow"><svg width="16" height="10"><path d="M0 5h14M10 1l4 4-4 4" stroke="#fff" stroke-width="1.6" fill="none"/></svg></span></div>
  <div style="display:flex;gap:10px;margin-top:22px">
    <span style="width:100px;height:30px;background:var(--white)" aria-label="Harbor Giving"></span>
    <span style="width:80px;height:30px;background:var(--white)" aria-label="Kindly Raise"></span>
    <span style="width:80px;height:30px;background:#3b5a9a" aria-label="Circle Social"></span>
    <span style="width:50px;height:30px;background:#3b5a9a"></span>
  </div>
</section>

<!-- support -->
<div class="photo" style="left:153px;top:3512px;width:568px;height:388px;background:radial-gradient(circle at 50% 50%,#c8465a 0%,#8a4060 35%,#3a2440 100%)" role="img" aria-label="Many hands joined together forming a heart shape"></div>
<div class="abs" style="left:1156px;top:3553px;width:44px;height:204px;background:var(--red)"></div>
<div class="abs" style="left:721px;top:3866px;width:479px;height:71px;background:var(--green)"></div>
<section class="abs" style="left:748px;top:3536px;width:300px">
  <h2 class="section-title">Support us</h2>
  <p class="body-text">Your donations allow us to provide medical care, health resources and supplies, and wellness education to the communities we serve. The links below are some of the ways you can donate to our organization.</p>
  <div class="cta"><span class="label">DONATE</span><span class="arrow"><svg width="16" height="10"><path d="M0 5h14M10 1l4 4-4 4" stroke="#fff" stroke-width="1.6" fill="none"/></svg></span></div>
</section>

<!-- about -->
<div class="photo" style="left:0;top:3860px;width:420px;height:140px;background:linear-gradient(180deg,rgba(255,255,255,0),rgba(200,170,150,.35))" role="img" aria-label="Faint joined hands fading into the page"></div>
<h2 class="section-title abs" style="left:153px;top:4020px">About Us</h2>
<div class="abs" style="left:0;top:4352px;width:1200px;height:289px;background:var(--orange)"></div>

<article class="card" style="left:153px">
  <div class="avatar" role="img" aria-label="Portrait of Dorla Penn"></div>
  <h3>DORLA PENN, FNP</h3><div class="role">( CO-FOUNDER )</div>
  <p>Dorla is a Family Nurse Practitioner currently practicing in her home state. She has spent many years working with underserved populations and has a passion for serving in global communities.</p>
  <span class="bio-btn">VIEW BIO</span>
</article>
<article class="card" style="left:384px">
  <div class="avatar" role="img" aria-label="Portrait of Wade Marlow" style="background:linear-gradient(160deg,#c7a58c,#6b4a3a)"></div>
  <h3>WADE MARLOW</h3><div class="role">( CO-FOUNDER )</div>
  <p>Wade is a retired nurse and former paramedic who has always loved helping others. He later earned a certificate in physical therapy and now supports our field teams.</p>
  <span class="bio-btn">VIEW BIO</span>
</article>
<article class="card" style="left:615px">
  <div class="avatar" role="img" aria-label="Portrait of Rosa Tembley" style="background:linear-gradient(160deg,#e2c29c,#a0704e)"></div>
  <h3>ROSA TEMBLEY, FNP</h3><div class="role">( CO-FOUNDER )</div>
  <p>Rosa is committed to her role in service to others and making a positive difference in the world. She also lives in a rural region and has travelled and worked in many areas.</p>
  <span class="bio-btn">VIEW BIO</span>
</article>
<article class="card" style="left:846px">
  <div class="avatar" role="img" aria-label="Portrait of Marina Kellet" style="background:linear-gradient(160deg,#e8cfae,#9c7a5c)"></div>
  <h3>MARINA KELLET, M.D.</h3><div class="role">( CO-FOUNDER )</div>
  <p>Marina grew up and remains in the mountain west. She moved to medicine after completing her medical residency and now practices in family care at a local clinic.</p>
  <span class="bio-btn">VIEW BIO</span>
</article>

<!-- contact -->
<footer class="contact-area">
  <h2>Contact Us</h2>
  <div class="abs" style="left:153px;top:152px;width:132px;height:52px;background:var(--white);display:flex;align-items:center;justify-content:center;gap:6px;font-family:Raleway,Arial,sans-serif;font-weight:700;font-size:10px;color:var(--purple-deep)"><span style="width:14px;height:14px;border-radius:50%;background:var(--red)"></span>Bright Meadow</div>
  <div class="col-title" style="left:153px;top:236px;font-size:12px">Follow us on</div>
  <span class="abs" style="left:153px;top:262px;width:18px;height:18px;border-radius:50%;background:var(--green)" aria-label="Circle Social"></span>
  <span class="abs" style="left:180px;top:262px;width:18px;height:18px;border-radius:50%;background:var(--green)" aria-label="Snapframe"></span>

  <div class="col-title" style="left:357px;top:148px">Links</div>
  <div class="col-list" style="left:357px;top:170px">HOME ›<br>MISSION ›<br>FUTURE ›<br>GET INVOLVED ›<br>ABOUT ›<br>CONTACT US ›</div>

  <div class="col-title" style="left:527px;top:148px">Contact</div>
  <div class="col-list" style="left:527px;top:172px;line-height:26px">
    <div><span style="display:inline-block;width:12px;height:12px;border-radius:50%;background:var(--white);margin-right:10px;vertical-align:-2px"></span>www.brightmeadowfoundation.org</div>
    <div><span style="display:inline-block;width:12px;height:12px;border-radius:50%;background:var(--white);margin-right:10px;vertical-align:-2px"></span>hello@brightmeadowfoundation.org</div>
    <div><span style="display:inline-block;width:12px;height:12px;border-radius:50%;background:var(--white);margin-right:10px;vertical-align:-2px"></span>1-555-014-2290</div>
  </div>

  <div class="field" style="top:150px">Name</div>
  <div class="field" style="top:194px">Email</div>
  <div class="field" style="top:238px;height:70px">Message</div>
  <div class="abs" style="left:987px;top:316px;width:60px;height:22px;background:var(--green);font-size:10px;font-weight:700;display:flex;align-items:center;justify-content:center">SEND</div>

  <div class="abs" style="left:0;top:402px;width:1200px;text-align:center;font-size:10px;opacity:.85">Copyright © 2019 Bright Meadow Foundation. All rights reserved.</div>
</footer>

</body>
</html>
```